vortane realty business card

We need a Business card for our new business. The logo was designed by ArtQuillo, and the text We want on the back is:
REAL ESTATE INVESTMENTS
- BUY, RENOVATE, SELL AND RENT RESIDENTIAL PROPERTIES
- FULL HOME REHABBING , REMODELING AND INTERIOR DESIGN
- HOME STAGING SERVICES
- WHOLESALE INVESTOR PROPERTIES
- MAKE CASH OFFERS ON HOUSES IN ANY CONDITION AND IN ANY SITUATION
- PRIVATE MONEY INVESTOR PROGRAMS WITH 6-12% RETURNS
- PAY CASH REWARDS FOR REFFERALS
- CONCIERGE SERVICE

```html
<!DOCTYPE html>
<html lang="en">
<head>
<meta charset="utf-8">
<title>Vortane Realty Business Card</title>
<link rel="stylesheet" href="https://fonts.googleapis.com/css2?family=Exo+2:wght@300;400;600;700&display=swap">
<style>
  :root {
    --page: #e9e8e6;
    --card: #fbfbfb;
    --ink: #2b2b2b;
    --muted: #5a5a5a;
    --grey-band: #a3a5a7;
    --cyan: #4fc3e0;
    --cyan-soft: #9adbee;
    --logo-grey: #8a8c8e;
  }
  * { box-sizing: border-box; margin: 0; padding: 0; }
  html, body { width: 1200px; height: 900px; overflow: hidden; }
  body {
    background: var(--page);
    font-family: "Exo 2", sans-serif;
    position: relative;
  }
  .card {
    position: absolute;
    top: 295px;
    width: 540px;
    height: 310px;
    background: var(--card);
    box-shadow: 0 2px 10px rgba(0,0,0,0.12);
    overflow: hidden;
  }
  .card--front { left: 40px; }
  .card--back { left: 620px; }

  .swoosh { position: absolute; left: 0; bottom: 0; width: 540px; height: 310px; }

  .contact { position: absolute; left: 30px; top: 28px; color: var(--ink); }
  .contact__name { font-weight: 700; font-size: 19px; letter-spacing: 0.3px; }
  .contact__title { font-size: 12px; color: var(--muted); margin-top: 2px; }
  .contact__list { list-style: none; margin-top: 16px; font-size: 11.5px; color: var(--muted); }
  .contact__list li { display: flex; align-items: center; gap: 8px; line-height: 18px; }
  .contact__list svg { width: 11px; height: 11px; fill: var(--ink); }

  .brand { text-align: left; }
  .card--front .brand { position: absolute; right: 40px; top: 140px; }
  .brand__row { display: flex; align-items: center; gap: 10px; }
  .brand__mark { width: 14px; height: 14px; background: var(--cyan); }
  .brand__name {
    font-weight: 400; font-size: 28px; color: var(--logo-grey);
    letter-spacing: 1px; text-transform: uppercase; line-height: 1.1;
  }
  .brand__tagline {
    font-weight: 300; font-size: 13px; color: var(--logo-grey);
    letter-spacing: 3px; margin-top: 2px; padding-left: 24px;
  }
  .website {
    position: absolute; right: 40px; bottom: 10px;
    font-size: 11px; color: #ffffff; letter-spacing: 0.5px;
  }

  .back-content {
    position: absolute; inset: 0;
    padding: 26px 36px 0;
    display: flex; flex-direction: column; align-items: center;
  }
  .services { margin-top: 16px; width: 100%; color: var(--muted); }
  .services__heading {
    font-weight: 600; font-size: 12.5px; color: var(--ink);
    letter-spacing: 1.5px; text-align: center; margin-bottom: 8px;
  }
  .services__list { list-style: none; font-size: 10px; letter-spacing: 0.3px; }
  .services__list li { display: flex; align-items: center; gap: 8px; line-height: 17px; }
  .services__list li::before {
    content: ""; flex: none; width: 5px; height: 5px; background: var(--cyan);
  }
</style>
</head>
<body>
  <section class="card card--front" aria-label="Business card front">
    <svg class="swoosh" viewBox="0 0 540 310" preserveAspectRatio="none" aria-hidden="true">
      <path d="M0 230 C150 300 330 290 540 270 L540 310 L0 310 Z" fill="var(--grey-band)"/>
      <path d="M0 210 C160 290 340 282 540 262 L540 270 C330 290 150 300 0 230 Z" fill="var(--cyan-soft)"/>
      <path d="M0 196 C170 282 350 274 540 254 L540 258 C345 278 165 288 0 204 Z" fill="var(--cyan)"/>
    </svg>

    <div class="contact">
      <div class="contact__name">Marco Ellison</div>
      <div class="contact__title">President</div>
      <ul class="contact__list">
        <li><svg viewBox="0 0 10 10"><path d="M2 0 L4 2.5 L3 3.5 C3.8 5 5 6.2 6.5 7 L7.5 6 L10 8 L8.5 10 C4 9.5 0.5 6 0 1.5 Z"/></svg>012 555 0147</li>
        <li><svg viewBox="0 0 10 10"><path d="M2 0 H8 V10 H2 Z M3 1 V8 H7 V1 Z"/></svg>012 555 0148</li>
        <li><svg viewBox="0 0 10 10"><path d="M0 2 H10 V8 H0 Z M1 3 L5 6 L9 3 Z" fill-rule="evenodd"/></svg>hello@vortane.com</li>
        <li><svg viewBox="0 0 10 10"><circle cx="5" cy="5" r="5"/></svg>www.vortanerealty.com</li>
      </ul>
    </div>

    <div class="brand">
      <div class="brand__row"><span class="brand__mark"></span><span class="brand__name">Vortane Realty</span></div>
      <div class="brand__tagline">REAL ESTATE SOLUTIONS</div>
    </div>

    <div class="website">www.vortanerealty.com</div>
  </section>

  <section class="card card--back" aria-label="Business card back">
    <div class="back-content">
      <div class="brand">
        <div class="brand__row"><span class="brand__mark"></span><span class="brand__name">Vortane Realty</span></div>
        <div class="brand__tagline">REAL ESTATE SOLUTIONS</div>
      </div>
      <div class="services">
        <div class="services__heading">REAL ESTATE INVESTMENTS</div>
        <ul class="services__list">
          <li>BUY, RENOVATE, SELL AND RENT RESIDENTIAL PROPERTIES</li>
          <li>FULL HOME REHABBING, REMODELING AND INTERIOR DESIGN</li>
          <li>HOME STAGING SERVICES</li>
          <li>WHOLESALE INVESTOR PROPERTIES</li>
          <li>MAKE CASH OFFERS ON HOUSES IN ANY CONDITION AND IN ANY SITUATION</li>
          <li>PRIVATE MONEY INVESTOR PROGRAMS WITH 6-12% RETURNS</li>
          <li>PAY CASH REWARDS FOR REFERRALS</li>
          <li>CONCIERGE SERVICE</li>
        </ul>
      </div>
    </div>
  </section>
</body>
</html>
```